PTA Business Card

Seeking design for a business card, standard size. It is going to be for myself in regards to PTA - details:

Hollis Fernway Elementary School
PTA President
Neil Brawley
555-208-3147
Brawl1984@mailnest.example

Requirement:
Facebook icon? "Hollis Fernway PTA Durn"
Twitter thing? I am new to twitter so not sure what to put, here is the link:
https://twitter.com/HFRoverbirdsPTA

I was thinking on the front would be a notebook paper background? Not a requirement but was thinking it would look cool?

Total freedom here, let your creativity spread because I don't have any suggestions for design, sorry. Colors of school district are black and yellow.

Backside I am not sure exactly what to put on it.

```html
<!DOCTYPE html>
<html lang="en">
<head>
<meta charset="utf-8">
<title>Hollis Fernway PTA – Business Card</title>
<link rel="stylesheet" href="https://fonts.googleapis.com/css2?family=Arimo:wght@700&family=Cinzel:wght@400;500&display=swap">
<style>
  :root {
    --backdrop: #e8e6e2;
    --card-white: #ffffff;
    --ink: #111111;
    --title-red: #c8321f;
    --school-red: #e0262a;
    --band-pink: #b5386e;
    --band-blue: #2e5fae;
    --icon-blue: #2ea3dc;
    --accent-yellow: #f7d21a;
    --accent-rose: #d07a9f;
    --paper-light: #f7f8fa;
    --paper-shade: #dfe3ea;
  }
  html, body {
    margin: 0;
    padding: 0;
    width: 1200px;
    height: 1200px;
    overflow: hidden;
    background: var(--backdrop);
  }
  .canvas {
    position: relative;
    width: 1200px;
    height: 1200px;
  }
  .card {
    position: absolute;
    left: 120px;
    width: 960px;
    height: 560px;
    background: var(--card-white);
    box-shadow: 0 4px 14px rgba(0,0,0,0.18);
  }
  .card--front { top: 25px; }
  .card--back { top: 625px; }
  .card svg { display: block; width: 960px; height: 560px; }

  .holder-name {
    font-family: "Arimo", Arial, sans-serif;
    font-weight: 700;
    font-size: 40px;
    fill: var(--ink);
  }
  .holder-role {
    font-family: "Arimo", Arial, sans-serif;
    font-weight: 700;
    font-size: 25px;
    fill: var(--title-red);
  }
  .contact-text {
    font-family: "Arimo", Arial, sans-serif;
    font-weight: 700;
    font-size: 22px;
    fill: var(--card-white);
  }
  .contact-text--long { font-size: 19px; }
  .school-name {
    font-family: "Cinzel", "Times New Roman", serif;
    font-weight: 500;
    font-size: 46px;
    fill: var(--ink);
  }
  .school-type {
    font-family: "Cinzel", "Times New Roman", serif;
    font-weight: 400;
    font-size: 34px;
    fill: var(--school-red);
  }
</style>
</head>
<body>
<main class="canvas">

  <section class="card card--front" aria-label="Front of card">
    <svg viewBox="0 0 798 467" preserveAspectRatio="none" xmlns="http://www.w3.org/2000/svg">
      <defs>
        <linearGradient id="cornerTone" x1="0" y1="0" x2="1" y2="0">
          <stop offset="0" stop-color="var(--accent-yellow)"/>
          <stop offset="0.6" stop-color="var(--accent-yellow)"/>
          <stop offset="1" stop-color="var(--accent-rose)"/>
        </linearGradient>
      </defs>
      <polygon class="corner-accent" points="0,0 570,0 255,161 0,195" fill="url(#cornerTone)"
               role="img" aria-label="Decorative fan of coloured triangles in yellow, gold, plum, lavender and rose"/>

      <text class="holder-name" x="498" y="130">Neil Brawley</text>
      <text class="holder-role" x="498" y="162">PTA President</text>

      <g class="contact-bands">
        <rect x="0" y="258" width="372" height="56" fill="var(--band-pink)"/>
        <rect x="372" y="258" width="426" height="56" fill="var(--band-blue)"/>
        <rect x="0" y="378" width="372" height="56" fill="var(--band-pink)"/>
        <rect x="372" y="378" width="426" height="56" fill="var(--band-blue)"/>
      </g>

      <g class="contact-badges" fill="var(--card-white)" stroke-width="2">
        <circle cx="72" cy="286" r="42" stroke="var(--band-pink)"/>
        <circle cx="412" cy="286" r="42" stroke="var(--band-blue)"/>
        <circle cx="72" cy="406" r="42" stroke="var(--band-pink)"/>
        <circle cx="412" cy="406" r="42" stroke="var(--band-blue)"/>
      </g>

      <g class="icon-phone" fill="var(--icon-blue)">
        <path d="M48,280 Q48,264 72,264 Q96,264 96,280 L86,282 L84,274 Q72,270 60,274 L58,282 Z"/>
        <path d="M56,284 L88,284 L94,306 L50,306 Z"/>
        <circle cx="72" cy="294" r="6" fill="var(--card-white)"/>
        <circle cx="72" cy="294" r="2.5"/>
      </g>

      <g class="icon-mail">
        <rect x="388" y="270" width="48" height="32" rx="2" fill="var(--icon-blue)"/>
        <polyline points="390,272 412,290 434,272" fill="none" stroke="var(--card-white)" stroke-width="3"/>
        <line x1="390" y1="300" x2="405" y2="285" stroke="var(--card-white)" stroke-width="2"/>
        <line x1="434" y1="300" x2="419" y2="285" stroke="var(--card-white)" stroke-width="2"/>
      </g>

      <text class="contact-text" x="135" y="294">555-208-3147</text>
      <text class="contact-text contact-text--long" x="468" y="293">Brawl1984@mailnest.example</text>
      <text class="contact-text" x="132" y="414">HFRoverbirdsPTA</text>
      <text class="contact-text" x="470" y="414">Hollis Fernway PTA</text>
    </svg>
  </section>

  <section class="card card--back" aria-label="Back of card">
    <svg viewBox="0 0 798 467" preserveAspectRatio="none" xmlns="http://www.w3.org/2000/svg">
      <defs>
        <linearGradient id="paperTone" x1="0" y1="0" x2="1" y2="1">
          <stop offset="0" stop-color="var(--paper-shade)"/>
          <stop offset="0.35" stop-color="var(--paper-light)"/>
          <stop offset="1" stop-color="var(--paper-shade)"/>
        </linearGradient>
      </defs>
      <rect class="paper-backdrop" x="0" y="0" width="798" height="467" fill="url(#paperTone)"
            role="img" aria-label="Photo of a sheet of lined spiral notebook paper with a mechanical pencil resting on it"/>
      <text class="school-name" x="170" y="232" textLength="433" lengthAdjust="spacingAndGlyphs">HOLLIS FERNWAY</text>
      <text class="school-type" x="172" y="278" textLength="431" lengthAdjust="spacingAndGlyphs">ELEMENTARY SCHOOL</text>
    </svg>
  </section>

</main>
</body>
</html>
```